依頼概要
第33回白鷺川大星火大会
2018年7月14日(土)午後7時30分開会
関東最大級22800発
三大花火師夢の饗宴 桐原煙火工業・宮田火工製作所・藤屋松井火工店
主催:北浜町観光協会・きたはまみなと祭り実行委員会
後援:北浜町・北浜町議会・七森町・北浜町商工会・七森町商工会・JA北陸あおば
問い合わせ:北浜町観光協会 TEL0280-81-1319
北浜町で検索的なもの
観覧チケットの購入はチケミナで検索的なもの

若干の構成を再度お願いする場合もあります。また、制作いただきました作品に、場合によりこちらで後援や開催日時等軽微な修正をする場合があります。
http://filevault-sample.jp/photo/3c1a9e07b42d58f6a0e9c2147bd86f03e5a1c9d2
上記URLは添付にあるものと同様の使用する写真です

町長様・観光協会様の方で候補作品から選んでいただきました。

ご参加・ご協力ありがとうございました。

```html
<!DOCTYPE html>
<html lang="ja">
<head>
<meta charset="utf-8">
<title>第33回白鷺川大星火大会</title>
<link rel="stylesheet" href="https://fonts.googleapis.com/css2?family=Noto+Sans+JP:wght@400;500;700;900&display=swap">
<style>
  :root {
    --night: #0b0d14;
    --ink: #1a1a1a;
    --paper: #ffffff;
    --white: #ffffff;
    --gold: #e9d9a6;
    --band: rgba(255,255,255,0.88);
    --box-line: #9a9a9a;
  }
  html, body { margin: 0; padding: 0; overflow: hidden; }
  body { width: 849px; height: 1200px; background: var(--paper); font-family: "Noto Sans JP", sans-serif; }
  .poster { position: relative; width: 849px; height: 1200px; overflow: hidden; background: var(--paper); }
  .fireworks-photo {
    position: absolute; left: 0; top: 0; width: 849px; height: 1045px;
    background:
      radial-gradient(ellipse 60% 30% at 50% 78%, rgba(232,214,160,0.55), transparent 70%),
      radial-gradient(ellipse 40% 25% at 20% 88%, rgba(180,90,170,0.45), transparent 70%),
      radial-gradient(ellipse 40% 25% at 80% 90%, rgba(120,160,90,0.4), transparent 70%),
      radial-gradient(ellipse 50% 30% at 55% 55%, rgba(200,190,150,0.35), transparent 70%),
      linear-gradient(180deg, #07080d 0%, #12131c 40%, #2a2630 75%, #3a3040 100%);
  }
  .year-mark {
    position: absolute; left: -40px; top: 500px;
    transform: rotate(-90deg); transform-origin: center;
    font-size: 190px; font-weight: 900; color: rgba(255,255,255,0.18);
    letter-spacing: 4px; line-height: 1;
  }
  .title { position: absolute; left: 56px; top: 30px; color: var(--white); font-weight: 900; margin: 0; line-height: 1; }
  .title .edition { display: block; font-size: 72px; letter-spacing: 2px; }
  .title .name { display: block; font-size: 88px; margin-top: 20px; letter-spacing: 0; }
  .schedule { position: absolute; right: 84px; top: 272px; text-align: right; color: var(--white); }
  .schedule .date { font-size: 46px; font-weight: 700; letter-spacing: 3px; margin: 0; }
  .schedule .time { font-size: 38px; font-weight: 500; margin: 10px 0 0; letter-spacing: 2px; }
  .scale-band {
    position: absolute; left: 420px; top: 436px; width: 345px; height: 40px;
    background: var(--band); color: var(--ink);
    font-size: 24px; font-weight: 700; line-height: 40px; text-align: center; letter-spacing: 1px;
  }
  .makers { position: absolute; left: 555px; top: 676px; color: var(--white); }
  .makers .lead { font-size: 22px; font-weight: 700; margin: 0 0 6px; color: var(--gold); }
  .makers ul { list-style: none; margin: 0; padding: 0; font-size: 15px; line-height: 1.4; }
  .footer { position: absolute; left: 0; top: 1045px; width: 849px; height: 155px; background: var(--paper); color: var(--ink); }
  .sponsors { position: absolute; left: 40px; top: 22px; font-size: 14px; line-height: 1.55; margin: 0; }
  .sponsors dt { float: left; width: 44px; }
  .sponsors dd { margin: 0 0 0 44px; }
  .contact { position: absolute; left: 40px; top: 110px; display: flex; align-items: center; gap: 10px; }
  .contact .label { font-size: 15px; }
  .contact .tel { font-size: 28px; font-weight: 700; letter-spacing: 1px; }
  .search { position: absolute; left: 555px; width: 262px; }
  .search .hint { font-size: 12px; margin: 0 0 4px; }
  .search .field { height: 26px; border: 1.5px solid var(--box-line); display: flex; align-items: center; justify-content: space-between; padding: 0 8px; font-size: 14px; font-weight: 500; }
  .search-info { top: 24px; }
  .search-ticket { top: 86px; }
</style>
</head>
<body>
<main class="poster">
  <div class="fireworks-photo" role="img" aria-label="夜空に広がる大きな打ち上げ花火の写真"></div>
  <div class="year-mark" aria-hidden="true">2018</div>

  <h1 class="title">
    <span class="edition">第３３回</span>
    <span class="name">白鷺川大星火大会</span>
  </h1>

  <div class="schedule">
    <p class="date">2018. 7. 14</p>
    <p class="time">午後７時３０分開会</p>
  </div>

  <div class="scale-band">関東最大級２２,８００発</div>

  <section class="makers">
    <p class="lead">三大花火師夢の饗宴</p>
    <ul>
      <li>桐原煙火工業</li>
      <li>宮田火工製作所</li>
      <li>藤屋松井火工店</li>
    </ul>
  </section>

  <footer class="footer">
    <dl class="sponsors">
      <dt>主催：</dt>
      <dd>北浜町観光協会・きたはまみなと祭り実行委員会</dd>
      <dt>後援：</dt>
      <dd>北浜町・北浜町議会・七森町・北浜町商工会</dd>
      <dd>七森町商工会・JA北陸あおば</dd>
    </dl>
    <div class="contact">
      <svg width="26" height="26" viewBox="0 0 24 24" aria-hidden="true"><path fill="#1a1a1a" d="M6.6 10.8a15.1 15.1 0 0 0 6.6 6.6l2.2-2.2a1 1 0 0 1 1-.25 11.4 11.4 0 0 0 3.6.57 1 1 0 0 1 1 1V20a1 1 0 0 1-1 1A17 17 0 0 1 3 4a1 1 0 0 1 1-1h3.5a1 1 0 0 1 1 1c0 1.25.2 2.45.57 3.57a1 1 0 0 1-.25 1z"/></svg>
      <span class="label">お問い合わせ</span>
      <span class="tel">0290-64-7725</span>
    </div>
    <div class="search search-info">
      <p class="hint">詳しくは、「北浜町」で検索！</p>
      <div class="field"><span>北浜町</span>
        <svg width="14" height="14" viewBox="0 0 16 16" aria-hidden="true"><circle cx="6.5" cy="6.5" r="4.5" fill="none" stroke="#1a1a1a" stroke-width="2"/><line x1="10" y1="10" x2="14.5" y2="14.5" stroke="#1a1a1a" stroke-width="2"/></svg></div>
    </div>
    <div class="search search-ticket">
      <p class="hint">観覧チケットは、「チケミナ」で検索！</p>
      <div class="field"><span>チケミナ</span>
        <svg width="14" height="14" viewBox="0 0 16 16" aria-hidden="true"><circle cx="6.5" cy="6.5" r="4.5" fill="none" stroke="#1a1a1a" stroke-width="2"/><line x1="10" y1="10" x2="14.5" y2="14.5" stroke="#1a1a1a" stroke-width="2"/></svg></div>
    </div>
  </footer>
</main>
</body>
</html>
```